Quenti Peruvian Cuisine needs a take-out menu

We need a new tri-fold 8.5"x11" take out menu for a Peruvian restaurant based in New Rochelle, NY. We have a vast selections of dishes from appetizers, seafood based dishes, desserts, Peruvian ceviches and more. We have attached the following:

Restaurant information
Pictures of our dishes
Quenti Logo in pdf format
Menu in word format
Old take out menu for reference only! (our dishes have changed)
Updates

Industry/Entity Type

Restaurant

```html
<!DOCTYPE html>
<html lang="en">
<head>
<meta charset="utf-8">
<title>Quenti Peruvian Cuisine – Take-Out Menu</title>
<link rel="stylesheet" href="https://fonts.googleapis.com/css2?family=Roboto+Condensed:wght@400;700&family=Lato:wght@300;400&family=Anton&display=swap">
<style>
:root{
  --brown:#9a5227;
  --brown-dk:#6f3517;
  --orange:#c24e1c;
  --green:#7bd843;
  --green-dk:#3f8f1f;
  --tag:#4b4b4b;
  --red:#e3231b;
  --paper:#f7f5f2;
  --ink:#3b2b22;
  --bg:#ececec;
}
*{box-sizing:border-box;margin:0;padding:0}
html,body{width:1200px;height:1200px;overflow:hidden;background:var(--bg)}
body{position:relative;font-family:"Roboto Condensed",Arial,sans-serif;color:var(--ink)}
.sheet{position:absolute;left:225px;width:750px;height:580px;display:flex;box-shadow:0 4px 14px rgba(0,0,0,.18)}
.sheet--outside{top:12px}
.sheet--inside{top:608px}
.panel{position:relative;width:250px;height:100%;overflow:hidden;padding:14px 16px 0}
.panel--light{background:linear-gradient(180deg,#fbfbfa,#ecebe8)}
.panel--dark{background:linear-gradient(180deg,#a65a2c 0%,#8a4620 55%,#733818 100%);color:#fff}
.tab{display:table;margin:6px auto 7px;padding:2px 12px;font-weight:700;font-size:11.5px;letter-spacing:.2px;text-transform:uppercase;clip-path:polygon(6px 0,calc(100% - 6px) 0,100% 50%,calc(100% - 6px) 100%,6px 100%,0 50%)}
.tab--orange{background:var(--orange);color:#eaf7c4}
.tab--green{background:var(--green);color:#2b1a10}
.grid{display:grid;grid-template-columns:1fr 1fr;column-gap:12px}
.item{margin-bottom:5px}
.item h3{font-size:9.5px;line-height:1.05;text-transform:uppercase;font-weight:700;color:var(--orange)}
.panel--dark .item h3{color:var(--green)}
.row{display:flex;align-items:flex-end;gap:4px}
.row p,.item>p{font-size:6.6px;line-height:1.15;flex:1}
.price{flex:none;font-size:8px;font-weight:700;padding:1px 4px;background:var(--tag);color:var(--green);min-width:28px;text-align:center}
.panel--dark .price{background:#fff;color:var(--ink);min-width:38px}
.sheet--inside .panel--light .price{background:var(--tag);color:#fff;min-width:38px}
.opts{display:flex;justify-content:space-between;font-size:6.6px;margin-top:2px}
.opts span{display:flex;gap:3px;align-items:center}
.choice{display:flex;justify-content:space-between;align-items:center;font-size:6.6px;border:1.5px solid #fff;border-radius:3px;background:#3c3c3c;color:#fff;padding:2px 5px;margin:2px 0 6px}
.choice b{background:var(--orange);color:#fff;padding:0 4px;font-size:7.5px}
.choice--green{background:var(--green);border-color:#c8f0a8;color:#2b1a10}
.choice--green b{background:var(--orange);color:#fff}
.choice--dark b{background:#fff;color:var(--orange)}
.chicken .item{margin-bottom:10px}
.photo{position:absolute;left:0;width:100%}
.cover-photo{top:0;height:270px;background:radial-gradient(circle at 55% 45%,#7a3a20 0%,#3d1f12 35%,#c9c2b8 62%,#e9e6e1 100%)}
.cover-brown{position:absolute;left:0;top:230px;width:100%;height:300px;background:linear-gradient(180deg,#a35a2c,#7e3f1b)}
.brand{position:absolute;top:36px;left:50%;transform:translateX(-50%);display:flex;align-items:center;gap:5px;background:#f6efd6;padding:6px 14px;border-radius:30px;border:2px solid var(--green-dk)}
.brand i{width:9px;height:9px;border-radius:50%;background:var(--green-dk)}
.brand span{font-family:"Roboto Condensed",sans-serif;font-weight:700;font-size:16px;color:var(--green-dk)}
.badge{position:absolute;left:60px;top:222px;width:126px;height:126px;border-radius:50%;background:var(--red);border:5px solid var(--green);outline:3px solid #fff;color:#fff;text-align:center;padding-top:26px}
.badge .b1{font-family:Lato,sans-serif;font-size:13px}
.badge .b2{font-family:Anton,sans-serif;font-size:25px;line-height:1.1}
.badge .b3{font-family:Lato,sans-serif;font-size:11.5px}
.headline{position:absolute;top:362px;width:100%;left:0;text-align:center;color:#fff;font-family:Lato,sans-serif;font-weight:300}
.headline .h1{color:var(--green);font-size:28px;line-height:1}
.headline .h2{font-size:62px;line-height:1.05;letter-spacing:1px}
.headline .h3{font-size:13.5px;margin-top:4px;font-weight:400}
.headline .h3 em{font-style:normal;color:var(--green)}
.contact{position:absolute;left:0;bottom:0;width:100%;height:70px;text-align:center;padding-top:24px;font-size:9px;color:#222;font-family:Lato,sans-serif}
.contact .phone{font-size:15px;font-family:Lato,sans-serif;font-weight:400}
.contact svg{vertical-align:-1px;margin-right:3px}
.swoosh{position:absolute;left:0;bottom:36px}
</style>
</head>
<body>

<section class="sheet sheet--outside">

  <div class="panel panel--light">
    <div class="tab tab--orange">Soups</div>
    <div class="grid">
      <div class="item"><h3>Aguadito Limeño</h3><p>chicken and vegetable soup mixed with rice and cilantro</p>
        <div class="row"><p>Large</p><span class="price">9.95</span></div>
        <div class="row"><p>Small</p><span class="price">5.95</span></div></div>
      <div class="item"><h3>Sopa a la Minuta</h3><div class="row"><p>traditional milk and angel's hair pasta soup, served with beef and eggs</p><span class="price">12.95</span></div></div>
      <div class="item"><h3>Caldo de Gallina</h3><div class="row"><p>hen broth with noodles, scallion, potatoes and hard-boiled eggs</p><span class="price">12.95</span></div></div>
      <div class="item"><h3>Chupe de Camarones Arequipeño</h3><div class="row"><p>shrimp soup mixed with rice, green peas, Cusco corn, milk, eggs and Peruvian spices</p><span class="price">15.95</span></div></div>
    </div>
    <div class="item"><h3>Parihuela del Puerto</h3><div class="row"><p>classic Peruvian seafood soup</p><span class="price">18.95</span></div></div>

    <div class="tab tab--orange">Ceviches</div>
    <div class="item"><h3>Leche de Tigre</h3><div class="row"><p>ceviche marinade in fresh lime juice</p><span class="price">9.95</span></div></div>
    <div class="item"><h3>Tiradito en Salsa de Aji Amarillo</h3><div class="row"><p>sashimi style fish in yellow pepper sauce and fresh lime juice, served with Cusco corn and sweet potatoes</p><span class="price">12.95</span></div></div>
    <div class="item"><h3>Piqueo Chalaco</h3><div class="row"><p>dish combined of Ceviche de Pescado (Fish Ceviche) and Jalea (Fried Seafood)</p><span class="price">23.95</span></div></div>
    <div class="item"><h3>Ceviche</h3><p>choice of raw fish, mixed seafood, shrimp or shrimp with octopus, marinated in fresh lime juice, served with red onions, Cusco corn and sweet potatoes</p>
      <div class="opts"><span>Pescado <b class="price">15.95</b></span><span>Camaron <b class="price">17.95</b></span></div>
      <div class="opts"><span>Mixto <b class="price">17.95</b></span><span>Camaron con Pulpo <b class="price">18.95</b></span></div></div>

    <div class="tab tab--orange">Sides</div>
    <div class="grid">
      <div>
        <div class="item"><h3>Papas Fritas</h3><div class="row"><p>french fries</p><span class="price">3.95</span></div></div>
        <div class="item"><h3>Arroz Blanco o Amarillo</h3><div class="row"><p>white/yellow rice</p><span class="price">3.95</span></div></div>
        <div class="item"><h3>Frejoles</h3><div class="row"><p>peruvian canario beans</p><span class="price">3.95</span></div></div>
      </div>
      <div>
        <div class="item"><h3>Maduros</h3><div class="row"><p>sweet plantains</p><span class="price">3.95</span></div></div>
        <div class="item"><h3>Tostones</h3><div class="row"><p>fried green plantains</p><span class="price">3.95</span></div></div>
        <div class="item"><h3>Yuca Frita</h3><div class="row"><p>fried yuccas</p><span class="price">3.95</span></div></div>
      </div>
    </div>
    <div class="photo" style="bottom:0;height:52px;background:linear-gradient(90deg,#8a5236 0%,#c7a48c 30%,#f0ece6 50%,#b98d5e 70%,#e5ddd3 100%);opacity:.55" role="img" aria-label="Photos of grilled beef and a yuca side dish"></div>
  </div>

  <div class="panel panel--dark chicken">
    <div class="tab tab--green">Chicken</div>
    <div class="grid">
      <div class="item"><h3>1/4 Pollo</h3><div class="row"><p>quarter chicken, served with two sides</p><span class="price">6.50</span></div></div>
      <div class="item"><h3>1/2 Pollo</h3><div class="row"><p>half chicken, served with two sides</p><span class="price">8.95</span></div></div>
      <div class="item"><h3>1 Pollo</h3><div class="row"><p>whole chicken, served with two sides</p><span class="price">16.95</span></div></div>
      <div class="item"><h3>Pollo Limeño</h3><div class="row"><p>whole chicken, served with French fries, avocado salad and yellow rice</p><span class="price">20.95</span></div></div>
      <div class="item"><h3>Pollo Chalaco</h3><div class="row"><p>whole chicken, served with avocado salad, salchipapa and yellow rice</p><span class="price">23.95</span></div></div>
      <div class="item"><h3>Pollo Quenti</h3><div class="row"><p>whole chicken, served with avocado salad, arroz chaufa (chicken or steak) and salchipapa</p><span class="price">30.95</span></div></div>
    </div>
    <div class="tab tab--green" style="margin-top:8px;margin-bottom:18px">Desserts</div>
    <div class="item" style="margin-bottom:11px"><h3>Crema Volteada</h3><div class="row"><p>Peruvian caramel custard</p><span class="price">5.95</span></div></div>
    <div class="item" style="margin-bottom:11px"><h3>Tres Leches</h3><div class="row"><p>Butter cake soaked in three kinds of milk</p><span class="price">5.95</span></div></div>
    <div class="item" style="margin-bottom:11px"><h3>Torta Helada</h3><div class="row"><p>Sponge cake topped with strawberry jello</p><span class="price">5.95</span></div></div>
    <div class="item" style="margin-bottom:11px"><h3>Torta de Chocolate</h3><div class="row"><p>Chocolate cake</p><span class="price">5.95</span></div></div>
    <div class="item"><h3>Picarones</h3><div class="row"><p>Peruvian style sweet potato doughnut covered with syrup</p><span class="price">5.95</span></div></div>
    <div class="photo" style="bottom:0;height:160px;background:radial-gradient(ellipse at 40% 40%,#d98a3a 0%,#b0601f 40%,#6e3414 80%)" role="img" aria-label="Photo of picarones, fried sweet potato doughnuts"></div>
  </div>

  <div class="panel" style="background:#fff;padding:0">
    <div class="photo cover-photo" role="img" aria-label="Photo of lomo saltado with rice"></div>
    <div class="cover-brown"></div>
    <div class="brand"><i></i><span>Quenti</span></div>
    <div class="badge"><div class="b1">Delivery Hours</div><div class="b2">Mon - Sun</div><div class="b3">11:30 am – 10 pm</div></div>
    <div class="headline">
      <div class="h1">Authentic Peruvian</div>
      <div class="h2">Cuisine</div>
      <div class="h3"><em>Deliveries on order of $15</em> or more<br>Chef's specials on weekends</div>
    </div>
    <svg class="swoosh" width="250" height="50" viewBox="0 0 250 50"><path d="M0 50 L0 32 Q125 -12 250 30 L250 50 Z" fill="#fff"/><path d="M0 32 Q125 -12 250 30" fill="none" stroke="#111" stroke-width="4"/></svg>
    <div class="contact">
      <div class="phone"><svg width="9" height="9" viewBox="0 0 24 24"><path d="M6.6 10.8a15 15 0 006.6 6.6l2.2-2.2a1 1 0 011-.25 11 11 0 003.6.6 1 1 0 011 1V20a1 1 0 01-1 1A17 17 0 013 4a1 1 0 011-1h3.5a1 1 0 011 1 11 11 0 00.6 3.6 1 1 0 01-.25 1z" fill="#333"/></svg>555-014-2277</div>
      <div><svg width="7" height="9" viewBox="0 0 24 32"><path d="M12 0a12 12 0 00-12 12c0 9 12 20 12 20s12-11 12-20A12 12 0 0012 0zm0 17a5 5 0 110-10 5 5 0 010 10z" fill="#333"/></svg>210 Harbor Ave. Bayport Vale, ST 00421</div>
      <div>www.QuentiKitchen.com</div>
    </div>
  </div>
</section>

<section class="sheet sheet--inside">

  <div class="panel panel--dark" style="padding-top:10px">
    <div class="tab tab--green" style="margin-top:0">Appetizers</div>
    <div class="item"><h3>Chicharron de Calamares</h3><div class="row"><p>crispy fried calamari served with house tartar sauce and salsa criolla</p><span class="price">12.95</span></div></div>
    <div class="item"><h3>Anticucho Carretillero</h3><p>choice chicken or cow's heart Peruvian style kebabs served with Cusco corn and grilled potatoes</p></div>
    <div class="choice choice--dark"><span>Corazon</span><b>15.95</b><span>Pollo</span><b>12.95</b></div>
    <div class="item"><h3>Palta Rellena</h3><p>peruvian avocado stuffed with choice of chicken or shrimp, marinated in Peruvian spices</p></div>
    <div class="choice choice--dark"><span>Camarones</span><b>11.95</b><span>Pollo</span><b>8.95</b></div>
    <div class="item"><h3>Tamal Criollo</h3><div class="row"><p>peruvian chicken tamale, served with salsa criolla</p><span class="price">5.95</span></div></div>
    <div class="item"><h3>Salchipapa</h3><div class="row"><p>french fries mixed with sliced hot dogs</p><span class="price">8.95</span></div></div>
    <div class="item"><h3>Papa a la Huancaina</h3><div class="row"><p>boiled potatoes, topped with aji amarillo and queso fresco sauce, egg, olives</p><span class="price">7.95</span></div></div>
    <div class="item"><h3>Ocopa Arequipeña</h3><div class="row"><p>boiled potatoes, topped with huacatay sauce and queso fresco, egg, olives</p><span class="price">7.95</span></div></div>
    <div class="item"><h3>Empanada Limeña</h3><div class="row"><p>patties stuffed with choice of chicken or beef</p><span class="price">3.95</span></div></div>
    <div class="item"><h3>Causa</h3><p>cold mashed potato infused with key of lime juice, pressed into a cake with choice of chicken or shrimp</p></div>
    <div class="choice choice--dark"><span>Camarones</span><b>9.95</b><span>Pollo</span><b>7.95</b></div>
    <div class="item"><h3>Choritos a la Chalaca</h3><div class="row"><p>steamed mussels topped with diced onions, tomatoes, lime juice and Cusco corn</p><span class="price">10.95</span></div></div>
    <div class="item"><h3>Piqueo Quenti</h3><div class="row"><p>Dish combined of Chicharron de Calamares, Papa a la Huancaina, Choritos a la Chalaca and Causa</p><span class="price">19.95</span></div></div>
    <div class="tab tab--green" style="margin:3px auto 4px">Salads</div>
    <div class="choice choice--dark"><span>ADD CHICKEN</span><b>3.95</b><span>ADD SHRIMP</span><b>5.95</b></div>
    <div class="item"><h3>Ensalada de la Casa</h3><div class="row"><p>lettuce, tomatoes, yellow peppers and zucchini</p><span class="price">6.95</span></div></div>
    <div class="item"><h3>Ensalada Quenti</h3><div class="row"><p>lettuce, tomatoes, cucumbers, red onions, carrots, radish and avocado</p><span class="price">7.95</span></div></div>
    <div class="item"><h3>Ensalada Cesar</h3><div class="row"><p>romaine lettuce, croutons, parmesan cheese and Quenti's special sauce</p><span class="price">8.95</span></div></div>
  </div>

  <div class="panel panel--light" style="padding-top:10px">
    <div class="tab tab--orange" style="margin-top:14px;background:linear-gradient(90deg,#c24e1c,#e0622a);color:#e4f7b5">Traditional Dishes</div>
    <div class="item"><h3>Parrillada Mixta</h3><div class="row"><p>dish combined of grilled NY Strip steak, anticuchos (Peruvian style kebabs), pork chops and sausage</p><span class="price">30.95</span></div></div>
    <div class="item"><h3>Churrasco en Salsa de Camarones</h3><div class="row"><p>NY strip steak topped with shrimps on hot yellow pepper sauce, served with rice</p><span class="price">19.95</span></div></div>
    <div class="item"><h3>Seco Norteño</h3><div class="row"><p>slowly cooked lamb stew in aji panka sauce, served with rice and Peruvian canario beans</p><span class="price">20.95</span></div></div>
    <div class="item"><h3>Seco de Pato Piurano</h3><div class="row"><p>slowly cooked duck stew in aji panka sauce, served with rice and hard-boiled yuccas</p><span class="price">17.95</span></div></div>
    <div class="item"><h3>Tallarines Verdes con Churrasco</h3><div class="row"><p>linguine pasta in Peruvian style pesto sauce served with grilled NY Strip steak</p><span class="price">17.95</span></div></div>
    <div class="item"><h3>Tacu Tacu</h3><p>peruvian canario beans mixed with rice, served with choice of NY Strip steak or wok-seared beef in soy sauce</p></div>
    <div class="choice choice--green" style="margin-top:6px;margin-bottom:10px"><span>Churrasco</span><b>17.95</b><span>Lomo</span><b>15.95</b></div>
    <div class="item"><h3>Churrasco a lo Pobre</h3><div class="row"><p>NY Strip steak served with fried eggs, sweet plantains, French fries and rice</p><span class="price">19.95</span></div></div>
    <div class="item"><h3>Lomo Saltado</h3><div class="row"><p>wok-seared steak, mixed with red onions, tomatoes, in soy sauce, served with fries and rice</p><span class="price">15.95</span></div></div>
    <div class="item"><h3>Pollo Saltado</h3><div class="row"><p>chicken, mixed with red onions, tomatoes, in soy sauce, served with fries and rice</p><span class="price">13.95</span></div></div>
    <div class="item"><h3>Aeropuerto</h3><div class="row"><p>peruvian style fried rice, mixed with noodles, chicken, beef and shrimp</p><span class="price">17.95</span></div></div>
    <div class="item"><h3>Arroz Chaufa</h3><p>peruvian style fried rice mixed with choice of beef or chicken</p></div>
    <div class="choice choice--green" style="margin-bottom:6px"><span>Carne</span><b>14.95</b><span>Pollo</span><b>12.95</b></div>
    <div class="item"><h3>Seco de Carne</h3><div class="row"><p>beef ribs stew in aji panka sauce, served with rice and Peruvian canario beans</p><span class="price">15.95</span></div></div>
    <div class="item"><h3>Aji de Gallina</h3><div class="row"><p>shredded chicken in a spicy aji amarillo creamy sauce, hard-boiled egg, olives, potatoes and rice</p><span class="price">11.95</span></div></div>
  </div>

  <div class="panel panel--dark" style="padding-top:10px">
    <div class="tab tab--green" style="margin-top:22px">Seafood</div>
    <div class="item" style="margin-bottom:11px"><h3>Pescado a lo Macho</h3><div class="row"><p>fried fish fillet topped with seafood in hot yellow pepper sauce, served with rice and yuccas</p><span class="price">19.95</span></div></div>
    <div class="item" style="margin-bottom:11px"><h3>Pescado Sudado</h3><div class="row"><p>corvina fish stew, in hot yellow pepper, tomatoes, onions, served with yuccas and rice</p><span class="price">16.95</span></div></div>
    <div class="item" style="margin-bottom:11px"><h3>Arroz con Mariscos</h3><div class="row"><p>peruvian style paella, red rice served with seafood</p><span class="price">17.95</span></div></div>
    <div class="item"><h3>Arroz Chaufa</h3><p>peruvian style fried rice served with choice of seafood or shrimp</p></div>
    <div class="choice choice--dark" style="margin-bottom:18px"><span>Mariscos</span><b>17.95</b><span>Camarones</span><b>16.95</b></div>
    <div class="item" style="margin-bottom:11px"><h3>Trucha Frita</h3><div class="row"><p>deep fried Trout, served with white rice, fried yuccas and salsa criolla</p><span class="price">17.95</span></div></div>
    <div class="item"><h3>Jalea</h3><p>deep fried mixed seafood and fish, served with fried yuccas</p></div>
    <div class="choice choice--dark"><span>Large</span><b>28.95</b><span>Small</span><b>17.95</b></div>
    <svg style="position:absolute;left:0;bottom:225px" width="250" height="40" viewBox="0 0 250 40"><path d="M0 40 Q125 -10 250 40 Z" fill="#fff"/><path d="M0 36 Q125 -12 250 36" fill="none" stroke="var(--green)" stroke-width="5"/></svg>
    <div class="photo" style="bottom:0;height:226px;background:radial-gradient(ellipse at 50% 55%,#e8a05a 0%,#8fae4a 22%,#f5f3ef 48%,#ffffff 100%)" role="img" aria-label="Photo of causa with shrimp served in an avocado half"></div>
  </div>
</section>

</body>
</html>
```